Mortgage Company ready to make a statement!

We have a basic logo that I am fairly happy with ... but it could use a little bit of tweaking before we order the sign for our building. We also want some knock-your-socks-off business cards.
Problem: Inside of our Mortgage Office (Tall Fern Mortgage Group), we are going to have a coffee lounge (Brewnook Cafe) for Realtors to use instead of the local Copperbean to meet with homebuyers. The office and coffee lounge are in an industrial building and is decorated with cozy overstuffed chairs, a hodge podge of interesting lamps and furniture, and goal is to make it as inviting as possible. However, we are a financial institution... so we need to keep it pretty clean as well.
One of my favorite marketing ideas is to cut a house key for everyone who buys a home using us with a key that matches our logo. There's only one key shape that works really well, so that needs to match the logo in order for the idea to work. I'll attach an image of the key blank.... although the way the key hole cut out looks terrible, so I was thinking of having them just do a thin outline instead.
Would like a similar, matching logo for the Brewnook Cafe... but possibly something that would be a little less formal and would be cute on a coffee mug- nothing stuffy.
AND, we're opening a home inspection company as well, and we would like that logo and branding to match. The home inspection company is "Tall Fern Home Inspections"
We were thinking that for the home inspection company , we could use a magnifying glass shape inside of the house shape for the logo, use a keyhole shape inside of the same house for the mortgage company, and use a coffee cup inside of the house shape for Brewnook Cafe.
Just getting stuck and need to help. I designed the attached logo myself, and that is what we are currently using. Designers at local printing companies have failed to impress us.
The mortgage industry has a lot of numbers and logos, etc that they require us to put on our business cards... so it's hard to keep them looking clean.
HELP! HELP! :)

```html
<!DOCTYPE html>
<html lang="en">
<head>
<meta charset="utf-8">
<title>Tall Fern Mortgage Group — Business Card</title>
<link rel="stylesheet" href="https://fonts.googleapis.com/css2?family=Cormorant+Garamond:wght@400&family=Montserrat:wght@700&family=Poppins:wght@400&display=swap">
<style>
  :root {
    --brand-blue: #246589;
    --paper: #ffffff;
    --backdrop: #ecebe6;
    --ink: #3c3c3c;
  }
  * { margin: 0; padding: 0; box-sizing: border-box; }
  html, body { width: 1200px; height: 929px; overflow: hidden; }
  body {
    background: var(--backdrop);
    position: relative;
    font-family: "Poppins", sans-serif;
  }
  .card {
    position: absolute;
    top: 310px;
    width: 520px;
    height: 310px;
    box-shadow: 0 6px 16px rgba(0,0,0,0.18);
    overflow: hidden;
  }
  .card--back { left: 50px; background: var(--brand-blue); }
  .card--front { left: 630px; background: var(--paper); }

  .wordmark {
    font-family: "Cormorant Garamond", serif;
    font-weight: 400;
    display: flex;
    align-items: center;
    gap: 10px;
    white-space: nowrap;
  }
  .wordmark__dot {
    width: 14px; height: 14px; border-radius: 50%;
    background: currentColor; flex: none;
  }
  .card--back .wordmark {
    position: absolute; left: 0; right: 0; top: 50%;
    transform: translateY(-50%);
    justify-content: center;
    color: var(--paper);
    font-size: 38px;
  }
  .card--front .wordmark {
    position: absolute; right: 30px; top: 40px;
    color: var(--brand-blue);
    font-size: 25px;
  }
  .card--front .wordmark__dot { width: 10px; height: 10px; }

  .name-band {
    position: absolute; left: 0; top: 88px;
    width: 255px; height: 56px;
    background: var(--brand-blue);
    color: var(--paper);
    padding: 8px 0 0 28px;
  }
  .name-band__name {
    font-family: "Cormorant Garamond", serif;
    font-size: 23px; letter-spacing: 1px; line-height: 1;
    text-transform: uppercase;
  }
  .name-band__title {
    font-family: "Montserrat", sans-serif;
    font-weight: 700; font-size: 13px; margin-top: 3px;
  }
  .address {
    position: absolute; right: 34px; top: 150px;
    text-align: right; color: var(--ink);
    font-size: 12px; line-height: 1.35; letter-spacing: 0.5px;
  }
  .contacts {
    position: absolute; left: 28px; bottom: 26px;
    list-style: none; color: var(--ink);
    font-size: 13px; letter-spacing: 0.6px; line-height: 1.45;
  }
  .contacts li { display: flex; align-items: center; gap: 10px; }
  .contacts svg { width: 11px; height: 11px; fill: var(--brand-blue); flex: none; }
</style>
</head>
<body>
  <section class="card card--back" aria-label="Card back">
    <div class="wordmark"><span class="wordmark__dot"></span>Tall Fern Mortgage Group</div>
  </section>

  <section class="card card--front" aria-label="Card front">
    <div class="wordmark"><span class="wordmark__dot"></span>Tall Fern Mortgage Group</div>
    <div class="name-band">
      <div class="name-band__name">Dana Whitlock</div>
      <div class="name-band__title">CEO</div>
    </div>
    <address class="address">Harbor Point Centre<br>Westbridge Avenue</address>
    <ul class="contacts">
      <li>
        <svg viewBox="0 0 12 12" aria-hidden="true"><path d="M3 0h6a1 1 0 0 1 1 1v10a1 1 0 0 1-1 1H3a1 1 0 0 1-1-1V1a1 1 0 0 1 1-1zm0 1.5v8h6v-8z"/></svg>
        000-555-0182
      </li>
      <li>
        <svg viewBox="0 0 12 12" aria-hidden="true"><path d="M3 0h6v3H3zM1 4h10a1 1 0 0 1 1 1v4H9.5v3h-7V9H0V5a1 1 0 0 1 1-1zm2.5 4v3h5V8z"/></svg>
        000-555-0182
      </li>
      <li>
        <svg viewBox="0 0 12 12" aria-hidden="true"><path d="M0 2h12v1L6 7 0 3zm0 2.2L6 8.2l6-4V10H0z"/></svg>
        dana.whitlock@tallfernmg.com
      </li>
    </ul>
  </section>
</body>
</html>
```